Wochen Speiseplan
Zielgruppe
Hospiz
Aufgabenstellung
Wir brauchen für unser Hospiz einen Wochenspeiseplan. Es soll eine Powerpointseite im A4 Format erstellt werden. Wir brauchen 4 unterschiedliche Seiten - für jede Jahreszeit einen Entwurf. Der Speiseplan soll von uns selbst ausgefüllt werden können.
Inhalte: Montag - Sonntag jeweils Mittag- und Abendessen. (Aufgebaut wie ein Stundenplan.). Möglichst große Schriftgröße. In der Fußnote bitte: "Änderungen vorbehalten schreiben". Das ganze soll professionell, aber dennoch liebevoll gestaltet sein. Es soll unseren Bewohnern "Liust machen" draufzuschauen. Der Plan wird jede Woche neu ausgefüllt, ausgedruckt und laminiert. Sollte also einfach zu handhaben sein.
Das Hospiz lebt von Spenden, daher bitte nicht zu aufwendig, dafür aber bezahlbar machen.

```html
<!DOCTYPE html>
<html lang="de">
<head>
<meta charset="utf-8">
<title>Wochenspeiseplan</title>
<link rel="stylesheet" href="https://fonts.googleapis.com/css2?family=Sniglet:wght@800&family=Lora:wght@400&family=Noto+Sans:ital,wght@0,400;1,700&display=swap">
<style>
  :root {
    --bg-yellow: #fdd45c;
    --bg-light: #fee08a;
    --banner-orange: #f39200;
    --banner-dark: #ee8400;
    --row-yellow: #f9e58c;
    --row-peach: #fde6d2;
    --header-white: #ffffff;
    --heading-orange: #f0861a;
    --text-dark: #1a1a1a;
    --grid-line: #ffffff;
  }
  * { margin: 0; padding: 0; box-sizing: border-box; }
  html, body { width: 1200px; height: 900px; overflow: hidden; }
  body { background: var(--bg-yellow); font-family: "Noto Sans", Verdana, sans-serif; color: var(--text-dark); }

  .menu-sheet { position: relative; width: 1200px; height: 900px; overflow: hidden; }

  .floral-backdrop {
    position: absolute; inset: 0;
    background:
      radial-gradient(circle at 12% 18%, var(--bg-light) 0, transparent 28%),
      radial-gradient(circle at 85% 92%, var(--bg-light) 0, transparent 30%),
      var(--bg-yellow);
  }

  .title-banner { position: absolute; left: 0; top: 0; width: 1200px; height: 260px; }

  .sheet-title {
    position: absolute; left: 298px; top: 52px;
    font-family: "Sniglet", "Chewy", cursive;
    font-weight: 800; font-size: 76px; line-height: 1;
    color: #fff; letter-spacing: 0.5px;
  }
  .sheet-greeting {
    position: absolute; left: 448px; top: 178px;
    font-family: "Lora", Georgia, serif;
    font-size: 29px; color: #fff;
    transform: rotate(-4.5deg); transform-origin: left center;
  }

  .meal-table {
    position: absolute; left: 37px; top: 258px; width: 1125px;
    border-collapse: collapse; table-layout: fixed;
    font-size: 21px; line-height: 1.3;
  }
  .meal-table col.day-col { width: 177px; }
  .meal-table col.lunch-col { width: 470px; }
  .meal-table col.dinner-col { width: 478px; }
  .meal-table th, .meal-table td {
    border: 2px solid var(--grid-line);
    vertical-align: top; text-align: left;
    padding: 8px 12px;
  }
  .meal-table thead th {
    background: var(--header-white); height: 67px;
    color: var(--heading-orange);
    font-size: 28px; font-style: italic; font-weight: 700;
    vertical-align: middle; padding-top: 4px;
  }
  .meal-table tbody tr { height: 73px; }
  .meal-table tbody tr:nth-child(odd) { background: var(--row-yellow); }
  .meal-table tbody tr:nth-child(even) { background: var(--row-peach); }
  .day-name { font-style: italic; font-weight: 700; }

  .footnote {
    position: absolute; right: 44px; top: 851px;
    font-size: 20px; font-style: italic; font-weight: 700;
  }
</style>
</head>
<body>
<main class="menu-sheet">
  <div class="floral-backdrop" role="img" aria-label="Dezentes florales Muster in hellen Gelbtönen als Hintergrund"></div>

  <svg class="title-banner" viewBox="0 0 1200 260" aria-hidden="true">
    <polygon points="252,0 1200,0 1200,186 262,252" fill="var(--banner-orange)"/>
    <rect x="1040" y="0" width="160" height="196" fill="var(--banner-dark)" opacity="0.35" role="img" aria-label="Florale Ornamente in Orange"/>
  </svg>

  <h1 class="sheet-title">Wochenspeiseplan</h1>
  <p class="sheet-greeting">Wir wünschen einen guten Appetit!</p>

  <table class="meal-table">
    <colgroup><col class="day-col"><col class="lunch-col"><col class="dinner-col"></colgroup>
    <thead>
      <tr><th></th><th>Mittagessen</th><th>Abendessen</th></tr>
    </thead>
    <tbody>
      <tr><th class="day-name">Montag</th><td>Spaghetti Bolognese</td><td>Gemüsepfanne mit Hähnchenbrust</td></tr>
      <tr><th class="day-name">Dienstag</th><td>Chicken Wrap mit buntem Salat<br>und Guacamole</td><td>Gebratener Seehecht in Ei-Hülle<br>dazu Kartoffelpüree</td></tr>
      <tr><th class="day-name">Mittwoch</th><td>Milchreis mit Zucker/Zimt<br>und Kirschkompott</td><td>Frikadelle schwäbische Art auf<br>Kräuterspätzle</td></tr>
      <tr><th class="day-name">Donnerstag</th><td>Nudeleintopf mit Geflügelfleisch</td><td>Gegrillte Schweinshaxe</td></tr>
      <tr><th class="day-name">Freitag</th><td>Germknödel mit Pflaumenmusfüllung</td><td>Nudel-Schinken-Gratin dazu<br>gemischter Salat</td></tr>
      <tr><th class="day-name">Samstag</th><td>3 gekochte Eier mit Senfsoße und<br>Kartoffeln</td><td>Kartoffelrösti mit Tomaten-Schnittlauch-<br>Quark</td></tr>
      <tr><th class="day-name">Sonntag</th><td>Linseneintopf mit Bockwurst,<br>Fladenbrot</td><td>Kochklopse Königsberger Art mit<br>Kartoffeln/Reis</td></tr>
    </tbody>
  </table>

  <p class="footnote">Änderungen vorbehalten</p>
</main>
</body>
</html>
```